Memphis Tournament

Tennis Tournament Poster - Size 11 X 17 inches

Court Clash Metro Open
April 4th - 7th, 2013
Brambleford Country Club & Holloway Tennis Center
Two Different Age Divisions for all levels - 18 up & 45 up
Men's, Women's, & Mixed - Singles and Doubles
All Levels - 2.5-Open
Non NCPA player welcomed
www.CourtClash.example
Updates

Need to change one thing and add another....

Two different age divisions for all divisions

should be

Two different age divisions for all levels

Also... need to add to the poster

Non NCPA players Welcomed

Industry/Entity Type

Club

Requirements
Nice to have
• Would like to have a place in the middle of the poster where I can attached kind of like a stack of sticky notes in the shape of a tennis ball and people can take one. So it would be nice if there was an image on the poster in the shape and size of a ball, preferable close to the middle for me to attach those.

```html
<!DOCTYPE html>
<html lang="en">
<head>
<meta charset="utf-8">
<title>Court Clash Metro Open 2013</title>
<link rel="stylesheet" href="https://fonts.googleapis.com/css2?family=Oswald:wght@500;700&family=Ribeye&family=Source+Sans+3:ital,wght@0,400;0,600;1,700&display=swap">
<style>
  :root {
    --paper: #ffffff;
    --clay: #d0683d;
    --clay-soft: #dc7a4f;
    --banner: #1f6b5b;
    --banner-shadow: #a9d4d0;
    --title-yellow: #f1dc5c;
    --ink: #2b2b2b;
    --wordmark: #3b3b3b;
    --accent-teal: #1f7a68;
    --ball-yellow: #fce86d;
  }
  * { margin: 0; padding: 0; box-sizing: border-box; }
  html, body { width: 776px; height: 1200px; overflow: hidden; background: var(--paper); }
  .poster { position: relative; width: 776px; height: 1200px; background: var(--paper); overflow: hidden; font-family: "Source Sans 3", Arial, sans-serif; color: var(--ink); }

  .player-art { position: absolute; left: 0; top: 0; width: 380px; height: 1200px; }

  .wordmark {
    position: absolute; left: 263px; top: 92px; width: 372px;
    text-align: center; font-family: "Oswald", sans-serif; font-weight: 700;
    font-size: 52px; line-height: 62px; letter-spacing: 1px; text-transform: uppercase;
    color: var(--wordmark);
  }

  .banner { position: absolute; left: 180px; top: 140px; width: 560px; height: 320px; }
  .banner-text { position: absolute; left: 193px; top: 214px; width: 525px; text-align: center; }
  .banner-year { font-family: "Oswald", sans-serif; font-weight: 700; font-size: 30px; color: #fff; letter-spacing: 1px; line-height: 40px; }
  .banner-year .chev { font-weight: 500; font-size: 20px; vertical-align: 4px; margin: 0 4px; }
  .banner-title { font-family: "Ribeye", cursive; color: var(--title-yellow); line-height: 1.1; font-weight: 400; }
  .banner-title .line1 { display: block; font-size: 38px; margin-top: 18px; }
  .banner-title .line2 { display: block; font-size: 58px; margin-top: 2px; }

  .take-one {
    position: absolute; left: 530px; top: 705px; width: 188px; height: 188px; border-radius: 50%;
    background: var(--ball-yellow); color: #fff; font-size: 28px; text-align: center;
    padding-top: 117px; font-weight: 400;
  }

  .event-details { position: absolute; right: 58px; top: 934px; text-align: right; }
  .event-dates { font-family: "Oswald", sans-serif; font-weight: 700; font-size: 18px; letter-spacing: 1.5px; line-height: 24px; }
  .event-venue { font-size: 16px; line-height: 22px; }
  .event-venue .small { font-size: 14px; }
  .event-divisions { margin-top: 20px; font-size: 14px; font-weight: 600; line-height: 22px; }
  .event-formats, .event-levels, .event-welcome { font-size: 14px; line-height: 24px; }
  .event-formats strong { color: var(--accent-teal); font-weight: 600; }
  .event-levels em { font-weight: 700; }
  .event-welcome { font-weight: 600; }
  .event-site { margin-top: 10px; font-size: 15px; font-weight: 600; line-height: 22px; color: var(--accent-teal); }
</style>
</head>
<body>
<main class="poster">
  <svg class="player-art" viewBox="0 0 380 1200" role="img" aria-label="Terracotta silhouette of a tennis player in a cap holding a racquet">
    <defs>
      <linearGradient id="clayFade" x1="0" y1="0" x2="1" y2="0">
        <stop offset="0" stop-color="#d0683d"/>
        <stop offset="1" stop-color="#dc7a4f" stop-opacity="0.85"/>
      </linearGradient>
    </defs>
    <rect x="0" y="0" width="380" height="1200" fill="url(#clayFade)"/>
  </svg>

  <div class="wordmark">Court Clash</div>

  <svg class="banner" viewBox="180 140 560 320" aria-hidden="true">
    <path d="M203,146 Q463,209 728,144 Q708,292 726,436 Q463,384 203,436 Q222,292 203,146Z" fill="var(--banner-shadow)"/>
    <path d="M193,154 Q455,216 718,154 Q698,300 718,446 Q455,392 193,446 Q212,300 193,154Z" fill="var(--banner)"/>
  </svg>

  <div class="banner-text">
    <div class="banner-year"><span class="chev">&gt;&gt;</span>2013<span class="chev">&lt;&lt;</span></div>
    <h1 class="banner-title"><span class="line1">Court Clash Metro</span><span class="line2">Open</span></h1>
  </div>

  <div class="take-one">Take One</div>

  <section class="event-details">
    <p class="event-dates">April 4th - 7th</p>
    <p class="event-venue">Brambleford Country Club</p>
    <p class="event-venue"><span class="small">and</span> Holloway Tennis Center</p>
    <p class="event-divisions">Two Different Age Divisions for all levels - 18 up &amp; 45 up</p>
    <p class="event-formats">Men's, Women's, &amp; Mixed - <strong>SINGLES</strong> &amp; <strong>DOUBLES</strong></p>
    <p class="event-levels">All Levels - 2.5-<em>Open</em></p>
    <p class="event-welcome">Non NCPA players Welcomed</p>
    <p class="event-site">www.CourtClash.example</p>
  </section>
</main>
</body>
</html>
```